Looking for a creative label design for our retail coffee bags

We are a coffee manufacturer (coffee roaster) looking to re-brand our retail label for our coffee bags. Our main coffee blend that we sell is our Harborline Velvet Blend. You can use this name when creating the label. We are going for a look that represents our company as a coffee roaster. Please reference our website (www.brindlemugworks.com) and our Facebook page to learn more about our company and to give you more inspiration on creating this design.

Target Market(s)

Retail customers/grocery stores

Industry/Entity Type

Manufacturer

Requirements
Must have
• The size of the label has to be 3" width x 4" height

Logo must be Black
Nice to have
• We currently incorporate a color on our labels for each blend. For example, Harborline Velvet Blend (royal blue), Decaffeinated Blend (red), Breakfast Blend (green), Flavored coffees (gold).

Rustic/vintage style

```html
<!DOCTYPE html>
<html lang="en">
<head>
<meta charset="utf-8">
<title>Brindle Mug Works – Retail Coffee Labels</title>
<link rel="stylesheet" href="https://fonts.googleapis.com/css2?family=Michroma&family=La+Belle+Aurore&display=swap">
<style>
  :root {
    --page-bg: #e9e9e9;
    --blend-blue: #13377d;
    --blend-red: #d62d3c;
    --blend-green: #19a64c;
    --blend-gold: #e3b43d;
    --ink: #1b1b1b;
    --logo-black: #161616;
    --paper-white: #ffffff;
  }
  * { box-sizing: border-box; margin: 0; padding: 0; }
  html, body { width: 1200px; height: 797px; overflow: hidden; }
  body {
    background: var(--page-bg);
    display: flex;
    align-items: center;
    justify-content: center;
    gap: 40px;
    font-family: "Michroma", sans-serif;
  }
  .label {
    position: relative;
    width: 255px;
    height: 340px;
    background-color: var(--blend);
    background-image:
      radial-gradient(ellipse at 30% 20%, rgba(255,255,255,0.08), transparent 60%),
      radial-gradient(ellipse at 80% 90%, rgba(0,0,0,0.14), transparent 65%);
    overflow: hidden;
  }
  .label--harborline { --blend: var(--blend-blue); }
  .label--decaf      { --blend: var(--blend-red); }
  .label--breakfast  { --blend: var(--blend-green); }
  .label--flavored   { --blend: var(--blend-gold); }

  .bean-art {
    position: absolute;
    left: 92px;
    top: 70px;
    width: 158px;
    height: 264px;
    background: radial-gradient(ellipse at 50% 75%, rgba(0,0,0,0.28), rgba(0,0,0,0.12) 55%, transparent 80%);
  }
  .label-art {
    position: absolute;
    inset: 0;
    width: 255px;
    height: 340px;
  }
  .blend-name   { font-family: "Michroma", sans-serif; fill: var(--paper-white); font-weight: 400; }
  .blend-name--main { font-size: 30px; }
  .blend-name--sub  { font-size: 19px; }
  .sketch-frame { fill: none; stroke: var(--ink); stroke-width: 0.8; opacity: 0.75; }
  .fresh-roasted {
    font-family: "La Belle Aurore", cursive;
    fill: var(--paper-white);
    font-size: 24px;
  }
  .logo-disc { fill: var(--logo-black); }
  .logo-ring { fill: none; stroke: rgba(255,255,255,0.5); stroke-width: 0.6; }
  .logo-name {
    font-family: "Michroma", sans-serif;
    fill: var(--paper-white);
    font-size: 10px;
  }
  .logo-tagline {
    font-family: "Michroma", sans-serif;
    fill: var(--paper-white);
    font-size: 4.2px;
    letter-spacing: 0.6px;
  }
</style>
</head>
<body>

  <!-- Harborline Velvet Blend -->
  <div class="label label--harborline">
    <div class="bean-art" role="img" aria-label="Hand-drawn sketch of scattered roasted coffee beans"></div>
    <svg class="label-art" viewBox="0 0 255 340">
      <path class="sketch-frame" d="M92 10 L234 11 L236 306"/>
      <g transform="translate(44,0) rotate(-90)">
        <text class="blend-name blend-name--main" x="-330" y="0" textLength="312" lengthAdjust="spacingAndGlyphs">HARBORLINE</text>
      </g>
      <g transform="translate(66,0) rotate(-90)">
        <text class="blend-name blend-name--sub" x="-330" y="0" textLength="312" lengthAdjust="spacingAndGlyphs">VELVET BLEND</text>
      </g>
      <g transform="rotate(-14 175 60)">
        <text class="fresh-roasted" x="150" y="58">fresh</text>
        <text class="fresh-roasted" x="128" y="84">roasted</text>
      </g>
      <defs><path id="arc-harborline" d="M128 262 A54 54 0 0 0 236 262"/></defs>
      <circle class="logo-disc" cx="182" cy="262" r="49"/>
      <circle class="logo-ring" cx="182" cy="262" r="44"/>
      <text class="logo-name" x="182" y="258" text-anchor="middle">BRINDLE</text>
      <text class="logo-name" x="182" y="273" text-anchor="middle">MUG WORKS</text>
      <text class="logo-tagline"><textPath href="#arc-harborline" startOffset="50%" text-anchor="middle">PROUDLY ROASTED IN MILLBROOK, PA SINCE 1994</textPath></text>
    </svg>
  </div>

  <!-- Decaffeinated Blend -->
  <div class="label label--decaf">
    <div class="bean-art" role="img" aria-label="Hand-drawn sketch of scattered roasted coffee beans"></div>
    <svg class="label-art" viewBox="0 0 255 340">
      <path class="sketch-frame" d="M92 10 L234 11 L236 306"/>
      <g transform="translate(44,0) rotate(-90)">
        <text class="blend-name blend-name--main" x="-330" y="0" textLength="312" lengthAdjust="spacingAndGlyphs">DECAFFEINATED</text>
      </g>
      <g transform="translate(66,0) rotate(-90)">
        <text class="blend-name blend-name--sub" x="-20" y="0" text-anchor="end" textLength="106" lengthAdjust="spacingAndGlyphs">BLEND</text>
      </g>
      <g transform="rotate(-14 175 60)">
        <text class="fresh-roasted" x="150" y="58">fresh</text>
        <text class="fresh-roasted" x="128" y="84">roasted</text>
      </g>
      <defs><path id="arc-decaf" d="M128 262 A54 54 0 0 0 236 262"/></defs>
      <circle class="logo-disc" cx="182" cy="262" r="49"/>
      <circle class="logo-ring" cx="182" cy="262" r="44"/>
      <text class="logo-name" x="182" y="258" text-anchor="middle">BRINDLE</text>
      <text class="logo-name" x="182" y="273" text-anchor="middle">MUG WORKS</text>
      <text class="logo-tagline"><textPath href="#arc-decaf" startOffset="50%" text-anchor="middle">PROUDLY ROASTED IN MILLBROOK, PA SINCE 1994</textPath></text>
    </svg>
  </div>

  <!-- Breakfast Blend -->
  <div class="label label--breakfast">
    <div class="bean-art" role="img" aria-label="Hand-drawn sketch of scattered roasted coffee beans"></div>
    <svg class="label-art" viewBox="0 0 255 340">
      <path class="sketch-frame" d="M92 10 L234 11 L236 306"/>
      <g transform="translate(44,0) rotate(-90)">
        <text class="blend-name blend-name--main" x="-330" y="0" textLength="312" lengthAdjust="spacingAndGlyphs">BREAKFAST</text>
      </g>
      <g transform="translate(66,0) rotate(-90)">
        <text class="blend-name blend-name--sub" x="-20" y="0" text-anchor="end" textLength="128" lengthAdjust="spacingAndGlyphs">BLEND</text>
      </g>
      <g transform="rotate(-14 175 60)">
        <text class="fresh-roasted" x="150" y="58">fresh</text>
        <text class="fresh-roasted" x="128" y="84">roasted</text>
      </g>
      <defs><path id="arc-breakfast" d="M128 262 A54 54 0 0 0 236 262"/></defs>
      <circle class="logo-disc" cx="182" cy="262" r="49"/>
      <circle class="logo-ring" cx="182" cy="262" r="44"/>
      <text class="logo-name" x="182" y="258" text-anchor="middle">BRINDLE</text>
      <text class="logo-name" x="182" y="273" text-anchor="middle">MUG WORKS</text>
      <text class="logo-tagline"><textPath href="#arc-breakfast" startOffset="50%" text-anchor="middle">PROUDLY ROASTED IN MILLBROOK, PA SINCE 1994</textPath></text>
    </svg>
  </div>

  <!-- Flavored Coffees -->
  <div class="label label--flavored">
    <div class="bean-art" role="img" aria-label="Hand-drawn sketch of scattered roasted coffee beans"></div>
    <svg class="label-art" viewBox="0 0 255 340">
      <path class="sketch-frame" d="M92 10 L234 11 L236 306"/>
      <g transform="translate(44,0) rotate(-90)">
        <text class="blend-name blend-name--main" x="-330" y="0" textLength="312" lengthAdjust="spacingAndGlyphs">FLAVORED</text>
      </g>
      <g transform="translate(66,0) rotate(-90)">
        <text class="blend-name blend-name--sub" x="-20" y="0" text-anchor="end" textLength="190" lengthAdjust="spacingAndGlyphs">COFFEES</text>
      </g>
      <g transform="rotate(-14 175 60)">
        <text class="fresh-roasted" x="150" y="58">fresh</text>
        <text class="fresh-roasted" x="128" y="84">roasted</text>
      </g>
      <defs><path id="arc-flavored" d="M128 262 A54 54 0 0 0 236 262"/></defs>
      <circle class="logo-disc" cx="182" cy="262" r="49"/>
      <circle class="logo-ring" cx="182" cy="262" r="44"/>
      <text class="logo-name" x="182" y="258" text-anchor="middle">BRINDLE</text>
      <text class="logo-name" x="182" y="273" text-anchor="middle">MUG WORKS</text>
      <text class="logo-tagline"><textPath href="#arc-flavored" startOffset="50%" text-anchor="middle">PROUDLY ROASTED IN MILLBROOK, PA SINCE 1994</textPath></text>
    </svg>
  </div>

</body>
</html>
```